Website Design Required For Education Video Portfolio Site

I am looking for a designer to create a skin for a relaunch of my website - www.brightfieldlearningfilms.co.uk. We want a clean and stylish new design.

The website showcases prospectus/promotional videos that are made for schools and colleges. Videos will be hosted on YouTube and embedded.

I want it to be stylish and clean.

I require 7 pages designed and this must be agreed in order to do the project.

1. Homepage
2. About
3. Prices
4. Testimonials
5. Contact Page with form
6. Promotional Videos
7. Subject Videos

The website will be then be built on the Wordpress system.

Target Market(s)

Education, Schools, Colleges, Universities

Industry/Entity Type

Education

Font styles to use
Serif

Colors

Designer to choose colors to be used in the design.

Requirements
Must have
• Video content, be clean, show our portfolio, descriptions about videos. I like the idea of having video headers.
Nice to have
• Images

```html
<!DOCTYPE html>
<html lang="en">
<head>
<meta charset="utf-8">
<title>Brightfield Learning Films — Educational Videos</title>
<link rel="stylesheet" href="https://fonts.googleapis.com/css2?family=Roboto:wght@400;500;700&family=Roboto+Condensed:wght@700&display=swap">
<style>
:root{
  --brand:#1aaeea;
  --ink:#111111;
  --muted:#8a8a8a;
  --body:#444444;
  --panel:#efefef;
  --footer:#3b3b3b;
  --footer-text:#9a9a9a;
  --white:#ffffff;
  --badge:#e4e7ea;
}
*{box-sizing:border-box;margin:0;padding:0}
html,body{width:1200px;height:2528px;overflow:hidden}
body{font-family:"Roboto",Arial,sans-serif;color:var(--ink);background:var(--white);position:relative}
.abs{position:absolute}

/* hero */
.hero{position:absolute;left:0;top:0;width:1200px;height:675px;overflow:hidden;
  background:
    radial-gradient(ellipse 420px 300px at 1010px 200px,rgba(18,16,17,.95) 0%,rgba(18,16,17,.6) 55%,rgba(18,16,17,0) 100%),
    radial-gradient(ellipse 380px 260px at 330px 330px,rgba(200,140,108,.95) 0%,rgba(176,118,88,.6) 55%,rgba(176,118,88,0) 100%),
    radial-gradient(ellipse 300px 260px at 120px 120px,rgba(150,118,86,.9) 0%,rgba(110,84,62,0) 100%),
    radial-gradient(ellipse 260px 200px at 470px 60px,rgba(215,220,226,.85) 0%,rgba(215,220,226,0) 100%),
    radial-gradient(ellipse 700px 220px at 700px 640px,rgba(224,220,214,.95) 0%,rgba(200,194,186,.7) 50%,rgba(200,194,186,0) 100%),
    radial-gradient(ellipse 220px 140px at 480px 500px,rgba(120,140,150,.8) 0%,rgba(120,140,150,0) 100%),
    linear-gradient(135deg,#6c5140 0%,#5a4a44 45%,#2a2627 75%,#1b1a1b 100%)}
.hero::after{content:"";position:absolute;inset:0;background:rgba(0,0,0,.12)}
.nav{position:absolute;z-index:2;top:24px;left:233px;width:734px;height:26px;display:flex;align-items:center;justify-content:space-between}
.logo{display:flex;align-items:center;gap:7px;color:var(--brand);font-weight:700;font-size:15px}
.logo i{width:20px;height:20px;background:var(--brand);border-radius:4px;display:block}
.menu{display:flex;gap:15px;font-size:8.5px;font-weight:500;color:var(--white);text-transform:uppercase}
.menu .on{color:var(--brand)}
.hero-kicker{position:absolute;z-index:2;top:314px;width:1200px;text-align:center;color:var(--white);font-size:14px}
.hero-title{position:absolute;z-index:2;top:326px;width:1200px;text-align:center;color:var(--white);font-size:40px;font-weight:700}
.hero-btn{position:absolute;z-index:2;left:522px;top:412px;width:156px;height:33px;border-radius:4px;background:rgba(140,132,128,.8);
  color:var(--white);font-size:15px;display:flex;align-items:center;justify-content:center}

/* intro */
.intro-title{left:234px;top:705px;width:230px;font-size:21px;font-weight:700;line-height:24.5px}
.intro-copy{left:234px;top:862px;width:228px;font-size:9.6px;line-height:11.8px;color:var(--muted)}
.intro-copy p+p{margin-top:12px}
.player{left:484px;top:706px;width:482px;height:271px;overflow:hidden;
  background:
    radial-gradient(ellipse 140px 110px at 160px 120px,#93ad62 0%,rgba(147,173,98,0) 100%),
    radial-gradient(ellipse 160px 200px at 400px 100px,#8e8f8c 0%,rgba(142,143,140,0) 100%),
    radial-gradient(ellipse 120px 90px at 260px 200px,#b7b6ae 0%,rgba(183,182,174,0) 100%),
    radial-gradient(ellipse 110px 140px at 40px 60px,#3f5a2a 0%,rgba(63,90,42,0) 100%),
    linear-gradient(135deg,#4f6b32 0%,#6f8a47 40%,#7d8a6a 70%,#5d6356 100%)}
.player .bar{position:absolute;left:0;bottom:0;width:100%;height:20px;background:rgba(0,0,0,.75)}
.player .track{position:absolute;left:34px;right:70px;bottom:9px;height:2px;background:#777}

/* pricing intro */
.budget-title{top:1036px;width:1200px;text-align:center;font-size:19.5px;font-weight:700}
.budget-copy{top:1072px;left:400px;width:400px;text-align:center;font-size:9.6px;line-height:11.8px;color:var(--body)}
.btn{background:var(--brand);color:var(--white);font-size:10px;font-weight:500;border-radius:4px;display:flex;align-items:center;justify-content:center}

/* video cards */
.thumb{top:1170px;height:200px}
.card-text{top:1380px;text-align:center}
.card-text h3{font-size:14px;font-weight:700}
.card-text .price{font-size:9.5px;margin:1px 0 4px}
.card-text p{font-size:7.8px;line-height:11.6px;color:var(--body)}
.dots{top:1467px;left:562px;display:flex;gap:7px}
.dots span{width:9px;height:9px;border-radius:50%;background:#ccc;display:block}
.dots .on{background:var(--brand)}

/* testimonials */
.testimonials{left:0;top:1508px;width:1200px;height:440px;background:var(--panel)}
.t-title{top:1541px;width:1200px;text-align:center;font-size:19.5px;font-weight:700}
.t-intro{top:1576px;left:400px;width:400px;text-align:center;font-size:9.6px;line-height:11.8px;color:var(--body)}
.quote{width:170px}
.quote .mark{font-size:58px;font-weight:700;line-height:40px;height:38px;color:var(--ink);font-family:Georgia,serif}
.quote p{margin-top:14px;font-size:8px;line-height:11.2px;color:var(--body);height:122px}
.who{font-family:"Roboto Condensed",Arial,sans-serif;font-weight:700;font-size:7.3px;line-height:10px;text-transform:uppercase}
.who b{font-size:8px;display:block}
.who span{font-size:6px;display:block;line-height:10px}

/* partners */
.p-title{top:1974px;width:1200px;text-align:center;font-size:19.5px;font-weight:700}
.badge{background:var(--badge);border-radius:50%}
.plate{background:var(--badge);border-radius:4px}

/* footer */
.footer{left:0;top:2293px;width:1200px;height:235px;background:var(--footer)}
.f-col{top:2340px;width:240px;color:var(--footer-text);font-size:8.3px;line-height:11.3px}
.f-col h4{color:var(--white);font-size:9px;font-weight:700;margin-bottom:23px}
.f-col a{color:var(--footer-text)}
.copy{left:230px;top:2445px;font-size:6.8px;color:var(--footer-text)}
</style>
</head>
<body>

<section class="hero" role="img" aria-label="Photo of two children leaning over an open storybook, one drawing with a pen">
  <nav class="nav">
    <div class="logo"><i></i>Brightfield Learning Films</div>
    <div class="menu">
      <span class="on">Home</span><span>About</span><span>Promotional Videos</span><span>Subject Videos</span><span>Testimonials</span><span>Prices</span><span>Contact Us</span>
    </div>
  </nav>
  <div class="hero-kicker">We make awesome</div>
  <h1 class="hero-title">Educational Videos</h1>
  <div class="hero-btn">Contact Us</div>
</section>

<h2 class="abs intro-title">Creating bespoke education videos to showcase schools, colleges &amp; training providers in the north of england</h2>
<div class="abs intro-copy">
  <p>Here at Brightfield Learning Films, we know how to create stylish, engaging, and successful educational videos for schools, colleges and training providers. We've been making them for years.</p>
  <p>We believe that when you're trying to attract new learners the best way to show how your learning establishment is better than the rest is with a compelling, top-quality video.</p>
</div>
<div class="abs player" role="img" aria-label="Embedded video: aerial view of a school and its playing field">
  <div class="bar"></div>
  <svg class="abs" style="left:8px;bottom:5px" width="10" height="10" viewBox="0 0 10 10"><path d="M2 1 L9 5 L2 9 Z" fill="#fff"/></svg>
  <div class="track"></div>
</div>

<h2 class="abs budget-title">Our Videos Won't Eat Up All Of Your Marketing Budget Either!</h2>
<p class="abs budget-copy">You see we do things differently at Brightfield Learning Films. Our highly experienced and dedicated team is small (but mighty) and that's how we keep costs low and affordable.</p>
<div class="abs btn" style="left:540px;top:1124px;width:117px;height:25px">View our prices</div>

<div class="abs thumb" style="left:0;width:30px;background:linear-gradient(160deg,#2d5a8c,#0f2440)" role="img" aria-label="Video still"></div>
<div class="abs thumb" style="left:48px;width:357px;background:
  radial-gradient(ellipse 90px 120px at 250px 130px,#2a2d4a 0%,rgba(42,45,74,0) 100%),
  radial-gradient(ellipse 70px 90px at 150px 150px,#3a3e60 0%,rgba(58,62,96,0) 100%),
  radial-gradient(ellipse 80px 200px at 335px 110px,#d9a25a 0%,rgba(217,162,90,0) 100%),
  radial-gradient(ellipse 160px 60px at 150px 20px,#e9e9ea 0%,rgba(233,233,234,0) 100%),
  linear-gradient(180deg,#b8a792 0%,#9c8874 60%,#5d6a8a 100%)" role="img" aria-label="Video still: two pupils outside a primary school entrance"></div>
<div class="abs thumb" style="left:422px;width:356px;background:
  radial-gradient(ellipse 130px 60px at 220px 95px,#d7a945 0%,rgba(215,169,69,0) 100%),
  radial-gradient(ellipse 90px 120px at 60px 140px,#2f48b0 0%,rgba(47,72,176,0) 100%),
  radial-gradient(ellipse 110px 110px at 300px 50px,#3b52b8 0%,rgba(59,82,184,0) 100%),
  radial-gradient(ellipse 120px 80px at 150px 20px,#efe9e7 0%,rgba(239,233,231,0) 100%),
  linear-gradient(160deg,#d9cfd2 0%,#6a76b6 50%,#263c98 100%)" role="img" aria-label="Video still: pupils playing trumpets in a school band"></div>
<div class="abs thumb" style="left:793px;width:356px;background:
  radial-gradient(ellipse 120px 130px at 180px 80px,#3f6fd4 0%,rgba(63,111,212,0) 100%),
  radial-gradient(ellipse 90px 110px at 40px 100px,#4f7a35 0%,rgba(79,122,53,0) 100%),
  radial-gradient(ellipse 110px 140px at 320px 120px,#7aa256 0%,rgba(122,162,86,0) 100%),
  linear-gradient(150deg,#6b8f4a 0%,#4f78c6 50%,#88ad62 100%)" role="img" aria-label="Video still: a blue school sign among green leaves"></div>
<div class="abs thumb" style="left:1168px;width:32px;background:linear-gradient(#a8b985,#6f8a50)" role="img" aria-label="Video still"></div>

<div class="abs card-text" style="left:48px;width:357px"><h3>Prospectus Videos (Interview based)</h3><div class="price">prices start at £1,200</div><p>Through interviews with the people who know it best (headteachers,principals, managers, parents, pupils and students) the prospectus video presents different aspects of life at your school, college or training organisation.</p></div>
<div class="abs card-text" style="left:432px;width:340px;top:1382px"><h3>Subject Videos</h3><div class="price">prices start at £1,200</div><p>We help you showcase your lessons via a series of 30-60 second videos for you to use across your website or social media. Highlight the wide variety of activities and lessons at your school.</p></div>
<div class="abs card-text" style="left:798px;width:346px"><h3>Promotional Videos (Music based)</h3><div class="price">prices start at £1,200</div><p>Affordable, music-driven videos that highlight your special events are an easy way to share school activities with families, visitors and OFSTED inspectors.</p></div>
<div class="abs dots"><span class="on"></span><span></span><span></span><span></span><span></span></div>

<section class="abs testimonials"></section>
<h2 class="abs t-title">Testimonials</h2>
<p class="abs t-intro">Discover what educators and administrators have to say about our transformative video solutions for schools. Hear directly from those who have experienced the power of our educational videos in enhancing learning outcomes and engagement.</p>

<div class="abs quote" style="left:234px;top:1652px"><div class="mark">“</div><p>I just wanted to say a huge thank you for our fabulous Christmas film. It is relaxed and organic and totally captures the spirit or the school. I love the fact it is all about the children. I can't wait to share it with the parent. Thanks again and we will definitely keep you in mind for future events and recommend you to other schools.</p><div class="who"><b>Clare Ashby</b><span>Head Teacher</span><span>Elmridge Primary School, Hollowby</span></div></div>
<div class="abs quote" style="left:422px;top:1652px"><div class="mark">“</div><p>A huge thanks to Owen for producing a fabulous promotional video for our school website. Throughout filming, both in school and on residential, he was flexible, highly creative and totally professional. He listened carefully to our requirements and provided excellent advice and expertise. The whole process went according to plan and we are delighted with the results.</p><div class="who"><b>Diane Rowell</b><span>Head Teacher</span><span>Fernside Colliery Primary School</span></div></div>
<div class="abs quote" style="left:609px;top:1652px"><div class="mark">“</div><p>The recording process ran very smoothly in school and I was very impressed with how much we managed to fit into a day! I appreciated the suggestions that Owen made so that we could capture some great parts of our school day; his expertise and eye for detail were invaluable.</p><div class="who"><b>Karen Dolby</b><span>Head Teacher</span><span>Ashcombe Green Primary School</span></div></div>
<div class="abs quote" style="left:797px;top:1652px"><div class="mark">“</div><p>We had an urgent need for a recording of a carol service and contacted BLF Creative to see if they could help. From the initial phone conversation, to the end product, the service was second to none. We would highly recommend</p><div class="who"><b>Helen Tarrant</b><span>Head Teacher</span><span>Bayview Primary School Marshfield, County Durham</span></div></div>

<div class="abs btn" style="left:521px;top:1891px;width:153px;height:25px">More Customer Stories</div>

<h2 class="abs p-title">Who We Work With</h2>
<div class="abs plate" style="left:228px;top:2036px;width:76px;height:72px" aria-label="Partner college"></div>
<div class="abs badge" style="left:392px;top:2034px;width:76px;height:76px" aria-label="Partner nursery"></div>
<div class="abs plate" style="left:543px;top:2054px;width:78px;height:34px" aria-label="Partner organisation"></div>
<div class="abs badge" style="left:700px;top:2032px;width:76px;height:76px" aria-label="Partner primary school"></div>
<div class="abs plate" style="left:852px;top:2052px;width:80px;height:38px" aria-label="Partner organisation"></div>
<div class="abs badge" style="left:242px;top:2160px;width:76px;height:76px" aria-label="Partner school"></div>
<div class="abs badge" style="left:392px;top:2158px;width:76px;height:76px" aria-label="Partner school"></div>
<div class="abs badge" style="left:543px;top:2156px;width:78px;height:78px" aria-label="Partner primary school"></div>
<div class="abs badge" style="left:694px;top:2156px;width:78px;height:78px" aria-label="Partner primary school"></div>
<div class="abs badge" style="left:844px;top:2156px;width:80px;height:80px" aria-label="Partner primary school"></div>

<footer class="abs footer"></footer>
<div class="abs f-col" style="left:234px"><h4>Our Mission</h4>Striving to deliver quality video content for schools and colleges in the North of England.</div>
<div class="abs f-col" style="left:484px"><h4>Contact us</h4><b>Phone:</b> 07700 900418<br><b>Email:</b> <a href="#">hello@brightfieldlearningfilms.co.uk</a></div>
<div class="abs f-col" style="left:734px"><h4>Visit</h4>Unit 4, Larkspur Business Park, Hollowby, Durham. DH8 2QT.</div>
<div class="abs copy">© Brightfield Learning Films Limited 2022. All Rights Reserved. Company Registration Number: 10482716.</div>

</body>
</html>
```